continuing medical education travel company. luxury, professional, quality service

PLEASE USE THE REVISED LOGO FOR ALL CARD DESIGNS, NO SNAKE HEAD

Target Market(s)

physicians

Industry/Entity Type

Travel Industry

Contact Information for Business Card

luxury quality, spot uv, foil, rounded corners

Colors
0255a3
3176b5
cfdeed
aaaaaa
5c5c5c

Requirements
Must have
• navy, platinum, possible holographic

```html
<!DOCTYPE html>
<html lang="en">
<head>
<meta charset="utf-8">
<title>Meridian Travel – Business Cards</title>
<link rel="stylesheet" href="https://fonts.googleapis.com/css2?family=Open+Sans:wght@400;600&display=swap">
<style>
  :root {
    --backdrop: #3b3633;
    --card: #141416;
    --card-edge: #222226;
    --navy: #2f2fa8;
    --platinum: #aaaaaa;
    --silver-light: #cfd3d8;
    --text: #f2f2f2;
    --muted: #8a8a8a;
    --rule: #6a6a6a;
  }
  * { box-sizing: border-box; margin: 0; padding: 0; }
  html, body {
    width: 1200px; height: 814px; overflow: hidden;
    background: var(--backdrop);
    font-family: "Open Sans", Arial, sans-serif;
  }
  .stage {
    width: 1200px; height: 814px;
    display: flex; align-items: center; justify-content: center; gap: 60px;
  }
  .card {
    position: relative;
    width: 520px; height: 297px;
    background: var(--card);
    border-radius: 14px;
    border: 1px solid var(--card-edge);
    box-shadow: 0 12px 30px rgba(0,0,0,.35);
    overflow: hidden;
  }
  /* brand lockup */
  .brand {
    display: flex; align-items: center; gap: 10px;
    color: var(--platinum);
    font-weight: 600;
    letter-spacing: .06em;
    white-space: nowrap;
  }
  .brand-dot {
    width: 12px; height: 12px; border-radius: 50%;
    background: var(--platinum);
  }
  /* front */
  .card-front .brand {
    position: absolute; top: 48px; right: 40px;
    font-size: 24px;
  }
  .card-front .divider {
    position: absolute; left: 40px; right: 40px; top: 132px;
    border-top: 1px solid var(--rule);
  }
  .address {
    position: absolute; right: 40px; top: 146px;
    text-align: right; color: var(--text);
    font-size: 13px; line-height: 19px;
  }
  .person {
    position: absolute; left: 40px; bottom: 30px;
  }
  .person-name { color: var(--navy); font-size: 18px; font-weight: 600; line-height: 22px; }
  .person-role { color: var(--muted); font-size: 13px; margin-bottom: 10px; }
  .contact-list { list-style: none; }
  .contact-list li {
    display: flex; align-items: center; gap: 9px;
    color: var(--text); font-size: 14px; line-height: 22px;
  }
  .contact-icon { width: 12px; height: 12px; flex: none; }
  /* back */
  .card-back {
    display: flex; flex-direction: column; align-items: center; justify-content: center;
  }
  .card-back .brand {
    font-size: 38px; color: var(--silver-light);
  }
  .card-back .brand-dot { width: 16px; height: 16px; background: var(--silver-light); }
  .web {
    margin-top: 26px; color: var(--text);
    font-size: 13px; letter-spacing: .2em;
  }
</style>
</head>
<body>
<main class="stage">

  <section class="card card-front" aria-label="Business card front">
    <div class="brand"><span class="brand-dot"></span>Meridian Travel</div>
    <div class="divider"></div>
    <address class="address" style="font-style:normal">
      48 Harbour Ave<br>Lakeview<br>QC H0H 2A4
    </address>
    <div class="person">
      <p class="person-name">Laura Bennett</p>
      <p class="person-role">Principal</p>
      <ul class="contact-list">
        <li>
          <svg class="contact-icon" viewBox="0 0 12 12" aria-hidden="true">
            <path d="M2.5 1h2l1 2.5-1.3 1a6 6 0 0 0 3.3 3.3l1-1.3 2.5 1v2c0 .6-.4 1-1 1A9.5 9.5 0 0 1 1.5 2c0-.6.4-1 1-1z" fill="var(--navy)"/>
          </svg>555.210.4870
        </li>
        <li>
          <svg class="contact-icon" viewBox="0 0 12 12" aria-hidden="true">
            <rect x="0.5" y="2" width="11" height="8" rx="1" fill="var(--navy)"/>
            <path d="M1 2.8 6 6.5l5-3.7" stroke="var(--card)" stroke-width="1" fill="none"/>
          </svg>lbennett@meridiantravel.com
        </li>
        <li>
          <svg class="contact-icon" viewBox="0 0 12 12" aria-hidden="true">
            <circle cx="6" cy="6" r="5.5" fill="var(--navy)"/>
            <path d="M.5 6h11M6 .5c2 2 2 9 0 11M6 .5c-2 2-2 9 0 11" stroke="var(--card)" stroke-width=".8" fill="none"/>
          </svg>www.meridiantravel.com
        </li>
      </ul>
    </div>
  </section>

  <section class="card card-back" aria-label="Business card back">
    <div class="brand"><span class="brand-dot"></span>Meridian Travel</div>
    <p class="web">www.meridiantravel.com</p>
  </section>

</main>
</body>
</html>
```